Business Image

I have recently had a new company logo made up and require some new business cards to go with it.

Target Market(s)

Developers & high worth clients.

Industry/Entity Type

Business

Contact Information for Business Card

The business is in the construction/management industry. It needs to be classy but have a industrial feel. I would like the business card to be a elegant presentation in itself.

Requirements
Must have
• Current logo & company name. Colouring needs to be the same as the current design also.
Nice to have
• A few different designs & presentations of single and double sided business cards.

```html
<!DOCTYPE html>
<html lang="en">
<head>
<meta charset="utf-8">
<title>Keystone Build Group – Business Card</title>
<link rel="stylesheet" href="https://fonts.googleapis.com/css2?family=Open+Sans:wght@400;600;700&display=swap">
<style>
  :root {
    --page-bg: #e6e6e6;
    --card-light: #f5f5f5;
    --card-mid: #dedede;
    --card-edge: #cfcfcf;
    --brand-navy: #1c2c45;
    --panel-navy-top: #34506f;
    --panel-navy-bottom: #1b2b43;
    --panel-dark-top: #23252b;
    --panel-dark-bottom: #131418;
    --name-text: #ece3d2;
    --detail-text: #c9bfae;
    --contact-text: #c8b48f;
  }
  * { margin: 0; padding: 0; box-sizing: border-box; }
  html, body {
    width: 1200px; height: 969px; overflow: hidden;
    background: var(--page-bg);
    font-family: "Open Sans", Arial, sans-serif;
  }
  .card {
    position: absolute; left: 100px; top: 200px;
    width: 1000px; height: 570px;
    background: linear-gradient(160deg, var(--card-light) 0%, var(--card-mid) 100%);
    border: 1px solid var(--card-edge);
    box-shadow: 0 12px 30px rgba(0,0,0,0.18);
    overflow: hidden;
  }
  .card-panels { position: absolute; inset: 0; width: 100%; height: 100%; }
  .brand {
    position: absolute; left: 0; right: 0; top: 46px;
    display: flex; flex-direction: column; align-items: center;
    color: var(--brand-navy); font-weight: 700;
  }
  .brand-mark {
    width: 110px; height: 110px; background: var(--brand-navy);
    margin-bottom: 30px;
  }
  .brand-name { font-size: 60px; line-height: 1; letter-spacing: 1px; }
  .brand-sub { font-size: 25px; letter-spacing: 4px; margin-top: 8px; }
  .holder { position: absolute; left: 40px; top: 392px; }
  .holder-name { font-size: 25px; font-weight: 700; color: var(--name-text); line-height: 34px; }
  .holder-title { font-size: 25px; color: var(--detail-text); line-height: 34px; }
  .holder-address { margin-top: 10px; font-size: 22px; color: var(--detail-text); line-height: 31px; font-style: normal; }
  .contacts {
    position: absolute; right: 30px; top: 393px;
    list-style: none; text-align: right;
  }
  .contacts li {
    display: flex; justify-content: flex-end; align-items: center;
    font-size: 22px; color: var(--contact-text); line-height: 32.5px;
  }
  .contacts svg { width: 18px; height: 18px; margin-left: 14px; fill: var(--contact-text); }
</style>
</head>
<body>
  <div class="card">
    <svg class="card-panels" viewBox="0 0 1000 570" preserveAspectRatio="none" aria-hidden="true">
      <defs>
        <linearGradient id="panelNavy" x1="0" y1="0" x2="0" y2="1">
          <stop offset="0" stop-color="var(--panel-navy-top)"/>
          <stop offset="1" stop-color="var(--panel-navy-bottom)"/>
        </linearGradient>
        <linearGradient id="panelDark" x1="0" y1="0" x2="0" y2="1">
          <stop offset="0" stop-color="var(--panel-dark-top)"/>
          <stop offset="1" stop-color="var(--panel-dark-bottom)"/>
        </linearGradient>
      </defs>
      <polygon points="0,274 512,425 512,570 0,570" fill="url(#panelNavy)"/>
      <polygon points="520,425 1000,274 1000,570 520,570" fill="url(#panelDark)"/>
    </svg>

    <div class="brand">
      <div class="brand-mark"></div>
      <div class="brand-name">KEYSTONE</div>
      <div class="brand-sub">BUILD GROUP</div>
    </div>

    <div class="holder">
      <div class="holder-name">DANIEL REEVE</div>
      <div class="holder-title">CEO/FOUNDER</div>
      <address class="holder-address">4120 Alder Crest Way<br>Fairbanks, Alaska 99701</address>
    </div>

    <ul class="contacts">
      <li>555 214 3087
        <svg viewBox="0 0 20 20"><path d="M2 7c0-3 4-4 8-4s8 1 8 4v2h-4V7H6v2H2z M5 10h10l2 7H3z"/></svg></li>
      <li>555 380 4129
        <svg viewBox="0 0 20 20"><path d="M6 1h8a1 1 0 0 1 1 1v16a1 1 0 0 1-1 1H6a1 1 0 0 1-1-1V2a1 1 0 0 1 1-1zm1 2v12h6V3zm3 13a1 1 0 1 0 0 2 1 1 0 0 0 0-2z"/></svg></li>
      <li>555 762 0518
        <svg viewBox="0 0 20 20"><path d="M5 2h10v5H5z M2 8h16v8h-3v-3H5v3H2z M6 14h8v4H6z"/></svg></li>
      <li>daniel@keystonebuild.com
        <svg viewBox="0 0 20 20"><path d="M2 4h16v12H2z M3 5l7 6 7-6" fill="none" stroke="var(--contact-text)" stroke-width="2"/></svg></li>
      <li>www.keystonebuild.com
        <svg viewBox="0 0 20 20"><circle cx="10" cy="10" r="8"/></svg></li>
    </ul>
  </div>
</body>
</html>
```